Web Design Project

Psychotherapy and Counselling Practice needs a landing page web design.

My business "Larkspur Advisory" specialises in the treatment of Anxiety and Depression with a holistic approach, endeavouring to unlock the key that holds us to ransom in a life that is imbalanced, frustrating, and ultimately of our own making due to our own perceptions and behaviours.

There is much that impacts us which we cannot change, but we are always in control of how we think, and how we frame our experiences.....learning to challenge those thoughts and behaviours that are destructive and disempowering opens up a world of joyful possibility. Life is about making choices, learn to make wiser and healthier choices.......

Larkspur Advisory has a client base of individual clients but will seek to expand to offer services to the Corporate world by offering an adjunct to employers for established "Wellness Programs".

Larkspur Advisory is a highly professional, ethically bound business, with the needs of the client at the forefront of all we do.

Larkspur Advisory wishes to avoid the usual "jargon driven" psychobabble offered on many counselling web pages. It aims to be stylishly presented, clean in look and with as few "words" as possible and a largely white background (faster loading and more powerful impact of what is stated), those words contained in the webpage should be meaningful, persuasive and have an impact simply at glance. Larkspur does not want , or expect, those prospective clients in need of support , to be reading through volumes of industry driven cliches.

At this point Larkspur is just looking for a high quality landing page. However in time this will likely expand to include other sections such as case studies, video content etc.

Target Market(s)

Those in need of emotional support, suffering mental health issues, and those simply wanting to become self aware supported by a mindful therapist.

Industry/Entity Type

Industry

Requirements
Must have
• The design must incorporate the Larkspur logo and colour schemes found on the attached files.

```html
<!DOCTYPE html>
<html lang="en">
<head>
<meta charset="utf-8">
<title>Larkspur Advisory – Wellness Landing Page</title>
<link href="https://fonts.googleapis.com/css2?family=Open+Sans:wght@300;400;600&display=swap" rel="stylesheet">
<style>
  :root {
    --green: #7fae1c;
    --green-dark: #6c9612;
    --green-light: #9cc63a;
    --band: #6d6d6d;
    --ink: #3d3d3d;
    --muted: #5a5a5a;
    --white: #ffffff;
    --page: #ffffff;
  }
  * { box-sizing: border-box; margin: 0; padding: 0; }
  html, body { width: 1200px; height: 1200px; overflow: hidden; background: var(--page); }
  body { font-family: "Open Sans", Arial, sans-serif; color: var(--ink); position: relative; }
  .abs { position: absolute; }

  /* Header */
  .brand { left: 216px; top: 108px; font-size: 54px; font-weight: 300; color: var(--green); letter-spacing: 1px; }
  .account { left: 560px; top: 26px; font-size: 11px; font-weight: 600; color: #222; }
  .account span { color: #999; margin: 0 6px; font-weight: 400; }
  .phone { left: 848px; top: 18px; font-size: 24px; font-weight: 400; color: #666; letter-spacing: .5px; }
  .phone b { color: var(--green); font-weight: 600; margin-right: 8px; }
  .main-nav { left: 519px; top: 68px; width: 509px; height: 47px;
    background: linear-gradient(#8fbd2a, var(--green-dark));
    display: flex; align-items: center; justify-content: space-around; padding: 0 12px;
    box-shadow: 0 6px 8px -4px rgba(0,0,0,.25); }
  .main-nav a { color: var(--white); text-decoration: none; font-size: 20px; font-weight: 600; text-transform: uppercase; }
  .main-nav i { width: 1px; height: 14px; background: rgba(255,255,255,.6); }
  .tagline { left: 557px; top: 121px; font-size: 38.5px; font-weight: 300; color: var(--green); white-space: nowrap; }
  .intro { left: 561px; top: 166px; font-size: 23px; font-weight: 400; color: #444; line-height: 30px; white-space: nowrap; }
  .search { left: 804px; top: 241px; width: 199px; height: 21px; border-radius: 11px;
    border: 2px solid #b5b5b5; background: linear-gradient(#e8e8e8, #ffffff);
    font-size: 10px; color: #555; padding: 2px 10px; }
  .search svg { position: absolute; right: 8px; top: 2px; }

  .social { display: flex; gap: 6px; }
  .social i { width: 24px; height: 24px; border-radius: 50%; background: #1f1f1f; border: 2px solid #fff; display: block; }
  .social-top { left: 382px; top: 272px; }
  .social-foot { left: 716px; top: 1139px; }
  .social-foot i { width: 26px; height: 26px; }

  /* Hero */
  .hero-bg { left: 0; top: 270px; }
  .hero-copy { left: 202px; top: 314px; font-size: 34px; font-weight: 300; color: var(--white); line-height: 45px; white-space: nowrap; }
  .hero-video { left: 628px; top: 299px; width: 388px; height: 260px; border: 5px solid #2a2a2a;
    background: radial-gradient(ellipse at 65% 40%, #d8d8d8 0%, #8a8a8a 25%, #1e1e1e 60%, #0b0b0b 100%); }

  /* Statement */
  .statement { left: 196px; top: 645px; font-size: 24px; line-height: 38px; color: var(--muted); white-space: nowrap; }
  .statement strong { color: var(--green); font-weight: 400; }
  .btn { display: block; background: var(--green); color: var(--white); font-size: 14px; font-weight: 600;
    text-transform: uppercase; text-align: center; text-decoration: none; }
  .btn-consult { left: 865px; top: 683px; width: 144px; height: 32px; line-height: 32px; }

  /* Features */
  .feature { top: 765px; width: 267px; height: 312px; text-align: center; }
  .feature h2 { font-size: 25px; font-weight: 400; color: var(--green); height: 42px; line-height: 42px; }
  .feature .photo { width: 267px; height: 115px; margin-top: 9px; border: 2px solid #ddd; }
  .feature p { font-size: 12.3px; line-height: 20px; color: #4a4a4a; margin: 14px 0 0; }
  .feature .btn { position: absolute; left: 61px; top: 279px; width: 144px; height: 32px; line-height: 32px; }
  .f1 { left: 183px; } .f2 { left: 460px; } .f3 { left: 737px; }
  .f1 p { padding: 0 14px; } .f2 p { padding: 0 12px; }
  .ph-team { background: linear-gradient(90deg, #a9a9a9, #e4e4e4 60%, #f2f2f2); }
  .ph-brain { background: radial-gradient(ellipse at center, #4a4a4a, #0d0d0d 70%); }
  .ph-talk { background: linear-gradient(90deg, #7a7a7a, #c8c8c8 45%, #5c5c5c); }
  .bar { width: 4px; height: 27px; background: var(--green); top: 773px; }
  .dots { width: 0; height: 140px; border-left: 1px dotted #aaa; top: 935px; }
  .rule { left: 165px; top: 1076px; width: 870px; height: 8px;
    background: radial-gradient(ellipse at center, rgba(0,0,0,.18), rgba(0,0,0,0) 70%); }

  /* Footer */
  .foot-nav { left: 196px; top: 1120px; font-size: 14px; color: #333; display: flex; gap: 8px; align-items: center; }
  .foot-nav i { width: 1px; height: 11px; background: #555; }
  .copyright { left: 196px; top: 1149px; font-size: 12px; color: #444; }
  .foot-brand-box { left: 845px; top: 1082px; width: 322px; height: 118px; background: #fff;
    box-shadow: 0 0 10px rgba(0,0,0,.05); }
  .foot-brand { left: 866px; top: 1132px; font-size: 27px; font-weight: 300; color: var(--green); letter-spacing: .5px; }
</style>
</head>
<body>

  <!-- Header -->
  <div class="abs brand">LARKSPUR</div>
  <div class="abs account">Login<span>|</span>Register</div>
  <div class="abs phone"><b>M</b>0400 118 275</div>

  <nav class="abs main-nav">
    <a href="#">Home</a><i></i><a href="#">About</a><i></i><a href="#">Services</a><i></i><a href="#">Contact</a><i></i><a href="#">FAQs</a>
  </nav>

  <div class="abs tagline">Your wellness starts today</div>
  <div class="abs intro">specialises in the treatment of Anxiety and<br>Depression with a holistic approach</div>

  <div class="abs search">Search
    <svg width="14" height="14" viewBox="0 0 14 14"><circle cx="5.5" cy="5.5" r="4" fill="none" stroke="#333" stroke-width="1.8"/><line x1="8.5" y1="8.5" x2="13" y2="13" stroke="#333" stroke-width="2"/></svg>
  </div>

  <!-- Hero band with curved edges -->
  <svg class="abs hero-bg" width="1200" height="360" viewBox="0 0 1200 360">
    <path d="M0 10 H1200 V290 C1120 300 1020 300 940 325 C860 350 780 362 720 352 C600 332 450 290 290 290 H0 Z" fill="var(--band)"/>
    <path d="M290 292 C450 292 600 336 720 356 C790 366 880 340 960 316 C880 348 790 372 720 362 C600 346 450 300 290 292 Z" fill="var(--green)"/>
    <path d="M0 0 H1200 V10 H0 Z" fill="#fff"/>
  </svg>
  <!-- Header swoosh -->
  <svg class="abs" style="left:170px;top:262px" width="630" height="20" viewBox="0 0 630 20">
    <path d="M0 16 C120 18 260 14 400 10 C480 8 560 6 630 5 C560 9 480 13 400 16 C260 20 120 20 0 19 Z" fill="var(--green)"/>
    <path d="M0 16 C120 17 220 13 330 10 C220 15 120 18 0 18 Z" fill="var(--green-light)"/>
  </svg>

  <div class="abs social social-top" aria-label="Social links"><i></i><i></i><i></i><i></i></div>

  <div class="abs hero-copy">Dr. MAE CORWIN<br>commitment to provide<br>quality healthcare for your<br>whole family drives<br>everything we do.</div>
  <div class="abs hero-video" role="img" aria-label="Video still: a person sitting alone against a wall, head in hands, backlit by a bright window"></div>

  <!-- Statement -->
  <p class="abs statement"><strong>Larkspur Advisory is a highly professional, ethically bound business,</strong><br>with the needs of the client at the forefront of all we do.</p>
  <a class="abs btn btn-consult" href="#">Consult Us</a>

  <!-- Features -->
  <div class="abs bar" style="left:451px"></div>
  <div class="abs bar" style="left:728px"></div>
  <div class="abs dots" style="left:455px"></div>
  <div class="abs dots" style="left:732px"></div>

  <section class="abs feature f1">
    <h2>Who We Are</h2>
    <div class="photo ph-team" role="img" aria-label="Photo of a smiling man in a group meeting"></div>
    <p>Lorem ipsum dolor sit amet, consectetuer adipiscing elit, sed diam nonummy nibh euismod tincidunt ut laoreet dolore magna aliquam erat volutpat.</p>
    <a class="btn" href="#">Get to Know Us</a>
  </section>
  <section class="abs feature f2">
    <h2>We’re Growing!</h2>
    <div class="photo ph-brain" role="img" aria-label="Illustration of a brain drawn as a circuit board"></div>
    <p>Ut wisi enim ad minim veniam, quis nostrud exerci tation ullamcorper suscipit lobortis nisl ut aliquip ex ea commodo consequat.</p>
    <a class="btn" href="#">How We Helps</a>
  </section>
  <section class="abs feature f3">
    <h2>Let’s Talk about You</h2>
    <div class="photo ph-talk" role="img" aria-label="Photo of a counsellor talking with a client"></div>
    <p>Duis autem vel eum iriure dolor in hendrerit in vulputate velit esse molestie consequat, vel illum dolore eu feugiat nulla facilisis at vero eros et accumsan et iusto odio.</p>
    <a class="btn" href="#">Consult Us</a>
  </section>

  <div class="abs rule"></div>

  <!-- Footer -->
  <nav class="abs foot-nav"><span>HOME</span><i></i><span>ABOUT</span><i></i><span>SERVICES</span><i></i><span>CONTACT</span><i></i><span>FAQS</span></nav>
  <div class="abs copyright">Copyright © 2013 Larkspur</div>
  <div class="abs social social-foot" aria-label="Social links"><i></i><i></i><i></i><i></i></div>
  <div class="abs foot-brand-box"></div>
  <div class="abs foot-brand">LARKSPUR</div>

</body>
</html>
```